Brightmoor Signal needs a Business Card

Designers!
More often than not, people want a cheap business card and often argue "I only want 100, not 500" - Years ago I worked in print and always wanted a client to ask for something that challenged me and would be great for my portfolio.

Years have past, and I dont have the time to do it myself so I'd love to see what everyone can offer.

Reason: Hey Guys, The designs are looking good but i've extended it a few more days as I wont be near a laptop and i'm trying to provide everyone feedback - Sorry!

Target Market(s)

Key decision makers, Potential Clients, Networking events and opportunities.

Industry/Entity Type

Business

Requirements
Must have
• Typography is very important. The type of paper is important.
The print, the shape. The creativity.
I'm very inspired by the below link
http://www.palevantro.com/blog/business-card-design/

Nice to have
• Stencelled cutouts. Embossing, nice typography.
I'd like the business card to be a conversation piece itself.

Attached is an image of business cards i've had in the past.
Additionally, some logos i've recently had designed by Quillmarsh.

```html
<!DOCTYPE html>
<html lang="en">
<head>
<meta charset="utf-8">
<title>Brightmoor Signal — Business Card</title>
<link rel="stylesheet" href="https://fonts.googleapis.com/css2?family=Source+Sans+3:wght@400;600&display=swap">
<style>
  :root {
    --page: #d6d7d9;
    --paper: #ffffff;
    --leaf: #8dc63f;
    --leaf-deep: #1f9a48;
    --navy: #0e3572;
    --sky: #3fa9dc;
    --stripe: #4f8fd6;
    --steel: #9a9c9f;
    --ink: #1d1d1f;
  }
  * { margin: 0; padding: 0; box-sizing: border-box; }
  html, body { width: 1200px; height: 780px; overflow: hidden; }
  body {
    background: var(--page);
    font-family: "Source Sans 3", sans-serif;
    position: relative;
  }
  .card {
    position: absolute;
    top: 220px;
    width: 520px;
    height: 340px;
  }
  .card--front { left: 50px; }
  .card--back { left: 630px; }
  .card__shape { position: absolute; inset: 0; width: 520px; height: 340px; }

  .brand {
    position: absolute;
    display: flex;
    align-items: center;
    gap: 12px;
    color: var(--navy);
    font-weight: 600;
    text-transform: uppercase;
    white-space: nowrap;
  }
  .brand__mark { background: var(--navy); flex: none; }

  .card--front .brand {
    left: 0; right: 0; top: 128px;
    justify-content: center;
    font-size: 36px; letter-spacing: 1px;
  }
  .card--front .brand__mark { width: 26px; height: 26px; }
  .card__rule {
    position: absolute; left: 100px; right: 100px; top: 186px;
    height: 1px; background: #c9cbcd;
  }
  .card__url {
    position: absolute; left: 0; right: 0; top: 192px;
    text-align: center;
    color: var(--leaf);
    font-size: 17px; letter-spacing: 5px;
  }

  .card--back .brand {
    left: 34px; top: 74px;
    font-size: 15px; letter-spacing: 0.5px; gap: 7px;
  }
  .card--back .brand__mark { width: 12px; height: 12px; }
  .contact {
    position: absolute; left: 110px; top: 118px;
    color: var(--ink);
  }
  .contact__name { font-size: 30px; font-weight: 400; margin-bottom: 6px; }
  .contact__line { font-size: 15px; line-height: 1.45; }
</style>
</head>
<body>

<div class="card card--front">
  <svg class="card__shape" viewBox="0 0 520 340" aria-hidden="true">
    <defs>
      <clipPath id="front-outline">
        <path d="M0 0 H225 L250 40 H520 V340 H235 L210 300 H0 Z"/>
      </clipPath>
      <linearGradient id="steel-fade" x1="0" x2="1">
        <stop offset="0" stop-color="#7d7f82"/>
        <stop offset="1" stop-color="#e3e4e5"/>
      </linearGradient>
    </defs>
    <g clip-path="url(#front-outline)">
      <rect width="520" height="340" fill="var(--paper)"/>
      <rect width="520" height="58" fill="var(--leaf)"/>
      <rect y="58" width="520" height="5" fill="var(--leaf-deep)"/>
      <rect x="250" y="76" width="270" height="5" fill="url(#steel-fade)"/>
      <rect y="236" width="520" height="3" fill="var(--sky)"/>
      <rect y="246" width="520" height="6" fill="url(#steel-fade)"/>
      <rect y="262" width="520" height="78" fill="var(--navy)"/>
      <polygon points="340,232 520,232 520,305 378,305" fill="var(--navy)"/>
      <g fill="var(--stripe)">
        <rect x="372" y="246" width="148" height="4"/>
        <rect x="378" y="256" width="142" height="4"/>
        <rect x="384" y="266" width="136" height="4"/>
        <rect x="390" y="276" width="130" height="4"/>
        <rect x="396" y="286" width="124" height="4"/>
      </g>
    </g>
  </svg>
  <div class="brand"><span class="brand__mark"></span>Brightmoor Signal</div>
  <div class="card__rule"></div>
  <div class="card__url">brightmoorsignal.com.au</div>
</div>

<div class="card card--back">
  <svg class="card__shape" viewBox="0 0 520 340" aria-hidden="true">
    <defs>
      <clipPath id="back-outline">
        <path d="M0 40 H270 L295 0 H520 V300 H310 L285 340 H0 Z"/>
      </clipPath>
      <linearGradient id="steel-fade-back" x1="0" x2="1">
        <stop offset="0" stop-color="#e3e4e5"/>
        <stop offset="1" stop-color="#7d7f82"/>
      </linearGradient>
    </defs>
    <g clip-path="url(#back-outline)">
      <rect width="520" height="340" fill="var(--paper)"/>
      <rect width="520" height="58" fill="var(--leaf)"/>
      <rect y="58" width="520" height="5" fill="var(--leaf-deep)"/>
      <rect x="0" y="104" width="290" height="5" fill="url(#steel-fade-back)"/>
      <rect y="228" width="520" height="3" fill="var(--sky)"/>
      <rect y="238" width="520" height="6" fill="url(#steel-fade-back)"/>
      <rect y="254" width="520" height="86" fill="var(--navy)"/>
      <polygon points="350,226 520,226 520,300 386,300" fill="var(--navy)"/>
      <g fill="var(--stripe)">
        <rect x="380" y="240" width="140" height="4"/>
        <rect x="386" y="250" width="134" height="4"/>
        <rect x="392" y="260" width="128" height="4"/>
        <rect x="398" y="270" width="122" height="4"/>
        <rect x="404" y="280" width="116" height="4"/>
      </g>
    </g>
  </svg>
  <div class="brand"><span class="brand__mark"></span>Brightmoor Signal</div>
  <div class="contact">
    <p class="contact__name">Callum Redfern</p>
    <p class="contact__line">Phone: 38650417</p>
    <p class="contact__line">Fax: 38650418</p>
    <p class="contact__line">Email: callum@brightmoor.au</p>
  </div>
</div>

</body>
</html>
```